Sales Flyer for Outdoor Kitchens

Looks to have a trifold flyer designed based off website content / projects. Use www.brickleafyardworks.com for content

```html
<!DOCTYPE html>
<html lang="en">
<head>
<meta charset="utf-8">
<title>Brickleaf Yardworks – Our Mission &amp; Values</title>
<link href="https://fonts.googleapis.com/css2?family=Gilda+Display&family=Poppins:wght@300&display=swap" rel="stylesheet">
<style>
  :root {
    --sand: #e3c7aa;
    --clay: #875a48;
    --ink-brown: #7a5242;
    --white: #ffffff;
  }
  html, body {
    margin: 0;
    padding: 0;
    overflow: hidden;
  }
  .flyer {
    position: relative;
    width: 1200px;
    height: 927px;
    overflow: hidden;
    background: var(--clay);
  }
  .mission-panel {
    position: absolute;
    left: 0;
    top: 0;
    width: 400px;
    height: 927px;
    background: var(--sand);
  }
  .shapes {
    position: absolute;
    left: 0;
    top: 0;
  }
  .heading {
    position: absolute;
    margin: 0;
    font-family: "Gilda Display", serif;
    font-weight: 400;
    font-size: 48px;
    line-height: 1;
    letter-spacing: -0.3px;
  }
  .body-copy {
    position: absolute;
    margin: 0;
    font-family: "Poppins", sans-serif;
    font-weight: 300;
    font-size: 14.3px;
    line-height: 19.3px;
  }
  .mission-heading { left: 38px; top: 44px; color: var(--ink-brown); }
  .mission-copy { left: 38px; top: 105px; width: 344px; color: var(--ink-brown); }
  .values-heading { left: 439px; top: 44px; font-size: 49px; color: var(--white); }
  .values-copy { left: 438px; top: 105px; width: 290px; color: var(--white); }
  .values-copy p { margin: 0 0 16px; }
</style>
</head>
<body>
<div class="flyer">
  <div class="mission-panel"></div>

  <svg class="shapes" width="1200" height="927" viewBox="0 0 1200 927">
    <defs>
      <linearGradient id="yardTone" x1="0.35" y1="0" x2="0.55" y2="1">
        <stop offset="0" stop-color="#b9cfdf"/>
        <stop offset="0.14" stop-color="#8fa56c"/>
        <stop offset="0.34" stop-color="#5f7440"/>
        <stop offset="0.48" stop-color="#a29a8a"/>
        <stop offset="0.6" stop-color="#7e9a55"/>
        <stop offset="0.72" stop-color="#8a8e91"/>
        <stop offset="0.86" stop-color="#55575a"/>
        <stop offset="1" stop-color="#6c6e72"/>
      </linearGradient>
      <linearGradient id="kitchenTone" x1="0" y1="0" x2="0.4" y2="1">
        <stop offset="0" stop-color="#5e615f"/>
        <stop offset="0.22" stop-color="#bcbcb6"/>
        <stop offset="0.45" stop-color="#d4d3cd"/>
        <stop offset="0.62" stop-color="#8fb06a"/>
        <stop offset="0.78" stop-color="#9d9c98"/>
        <stop offset="1" stop-color="#c4c2bd"/>
      </linearGradient>
      <linearGradient id="pavilionTone" x1="0" y1="0" x2="0" y2="1">
        <stop offset="0" stop-color="#a05a2c"/>
        <stop offset="0.25" stop-color="#8a4d2a"/>
        <stop offset="0.45" stop-color="#6e9a4a"/>
        <stop offset="0.62" stop-color="#86b35a"/>
        <stop offset="0.8" stop-color="#7b6a55"/>
        <stop offset="1" stop-color="#5e5044"/>
      </linearGradient>
      <linearGradient id="grillTone" x1="0" y1="0" x2="0" y2="1">
        <stop offset="0" stop-color="#4f86d6"/>
        <stop offset="0.28" stop-color="#9fb8d6"/>
        <stop offset="0.4" stop-color="#5a5650"/>
        <stop offset="0.6" stop-color="#c9bfae"/>
        <stop offset="0.8" stop-color="#6e6b66"/>
        <stop offset="1" stop-color="#8d8a85"/>
      </linearGradient>
    </defs>

    <polygon class="hero-photo" role="img" aria-label="Backyard fire pit area with a cut-metal sphere fire feature surrounded by grey Adirondack chairs on gravel, tall pines and a wooden fence behind"
      points="937,0 1200,0 1200,927 400,927" fill="url(#yardTone)"/>

    <polygon class="project-photo" role="img" aria-label="Covered patio outdoor kitchen with stone counters, sink and built-in grill opening onto a lawn"
      points="23,496 92,370 243,370 315,496 243,622 92,622" fill="url(#kitchenTone)"/>

    <polygon class="project-photo" role="img" aria-label="Cedar pavilion with chandelier over wicker seating around a fire table, open lawn beyond"
      points="252,629 311,503 472,503 544,629 472,755 311,755" fill="url(#pavilionTone)"/>

    <polygon class="project-photo" role="img" aria-label="Stacked stone outdoor kitchen island with stainless grill and storage doors on a tiled patio"
      points="23,766 92,640 243,640 315,766 243,892 92,892" fill="url(#grillTone)"/>
  </svg>

  <h1 class="heading mission-heading">Our Mission</h1>
  <p class="body-copy mission-copy">At Brickleaf Yardworks, we set new standards for outdoor living through innovative design and expert craftsmanship. Our goal is to surpass expectations by creating outdoor spaces that seamlessly blend with nature and reflect your unique personality. Whether you desire a serene getaway or a vibrant entertainment area, we're committed to realizing your vision. Experience the tranquility of nature in comfort with our tailored outdoor living spaces, including customized patios, elegant pergolas, and stylish fire features for relaxation and entertainment.</p>

  <h2 class="heading values-heading">Our Values</h2>
  <div class="body-copy values-copy">
    <p>Our deep passion for outdoor design drives our commitment to excellence, where meticulous attention to detail ensures every aspect contributes to enhancing your quality of life through personalized outdoor spaces crafted in collaboration with you.</p>
    <p>Get in touch with us today to start turning your outdoor space into a personalized haven.</p>
  </div>
</div>
</body>
</html>
```